Website Design Front page Holistic Members site & Natural Therapist Directory

I need a modern, fresh unique look for a natural therapy and holistic/ Spiritual directory & educational website. It needs to be clear, colourful, inviting and suitable for both sexes - young and old. I want it look fresh and super modern.

I will require the design in .psd format and anything in the centre section including rotational image needs to be supplied in .ai so I can break down the components and colours used will also be needed for frames and banners.

Target Market(s)

all ages, male and female. It must appeal to both therapists and general public.

Requirements
Must have
• Logo obviously. Room for a video player 300 x 250. And small introduction text panel. Must follow the layout in file attached. Also a rotating image up the top, in main section (have supplied example image alter as you like - man pointing top right). Have also supplied example of text to have on it. 16 Menu bars on left frame, under home. Must have 6 prominent links to main pages of site. Have included images use if you want or else use your own. These 6 are, Find a Psychic/ Medium, Find a Natural Therapist, Find a Business/ Club/ School, Find an Event/ Workshop, Find a Product, Holistic Career Centre.I have also attached a shot of the emag, although nothing special in design, useful for complimentary colour choices but not limited to. Another link image/ banner would be Free Chat Now.Another if room and not over crowded would be compare memberships. Can use leader board and leader ad board. Also require the footer to be designed and delivered in .ai similar to forma peak with link image to mingleroo and quillo.
Nice to have
• Compare memberships link would be great but not essential... don't want page to look too busy.
Should not have
• Must not be too busy.. think zen with a modern twist.

```html
<!DOCTYPE html>
<html lang="en">
<head>
<meta charset="utf-8">
<title>Aurora Hearth – Holistic Community</title>
<link rel="stylesheet" href="https://fonts.googleapis.com/css2?family=Open+Sans:ital,wght@0,400;0,600;0,700;1,600&display=swap">
<style>
:root{
  --sky-top:#8cc0ee;
  --sky-light:#eef6fd;
  --blue-label:#1f63b5;
  --blue-btn:#1c5fb8;
  --blue-soft:#6aa6e4;
  --orange:#f7941d;
  --orange-light:#fbb040;
  --orange-deep:#f37021;
  --yellow:#fdd23e;
  --green:#8cc63f;
  --teal:#3fc0cc;
  --purple:#92278f;
  --pink:#ec4195;
  --gold:#fbb03b;
  --title-blue:#2f7fd0;
  --text:#222;
  --white:#fff;
  --footer-text:#fff6d6;
  --footer-head:#d9731b;
}
*{box-sizing:border-box;margin:0;padding:0}
html,body{width:1200px;height:1198px;overflow:hidden}
body{font-family:Arial,Helvetica,sans-serif;color:var(--text);background:var(--white)}
.page{position:relative;width:1200px;height:1198px;overflow:hidden;
  background:linear-gradient(#fff 0,#f4f9fe 560px,#e3f0fb 720px,#eef5fc 722px,#eef5fc 960px)}
.abs{position:absolute}

/* header */
.site-header{left:0;top:0;width:1200px;height:127px;
  background:radial-gradient(ellipse at 20% 0,#bcd9f5 0,transparent 60%),linear-gradient(#a9cdf1,#e8f2fc 80%,#fff)}
.brand{left:190px;top:38px;display:flex;align-items:center;gap:8px}
.brand-dot{width:22px;height:22px;border-radius:50%;background:var(--pink)}
.brand-name{font-family:"Open Sans",sans-serif;font-weight:700;font-size:27px;color:#1a1a1a;letter-spacing:-.5px}
.login label{position:absolute;font-size:11px;font-weight:700;color:var(--blue-label)}
.login .field{position:absolute;top:46px;width:154px;height:23px;background:#fff;border:1px solid #c9dcef;box-shadow:inset 0 1px 2px rgba(0,0,0,.1)}
.login-btn{left:951px;top:47px;width:62px;height:21px;background:linear-gradient(#2d74cc,#1452a6);color:#fff;font-size:12px;font-weight:700;text-align:center;line-height:21px;border-radius:2px}
.forgot{left:613px;top:80px;width:221px;height:22px;background:var(--blue-soft);color:#fff;font-size:10.5px;font-weight:700;line-height:22px;text-align:center}

/* nav */
.main-nav{left:0;top:126px;width:1200px;height:36px;background:linear-gradient(var(--orange-light),var(--orange) 60%,#f58a1f);display:flex;padding-left:207px;align-items:center}
.main-nav a{color:#fff;text-decoration:none;font-size:13.5px;padding:0 7px;border-right:1px solid rgba(255,255,255,.45);line-height:26px;letter-spacing:.2px}
.main-nav a:last-child{border-right:0}

/* content panel */
.content-panel{left:156px;top:162px;width:888px;height:560px;background:linear-gradient(#fff,#f8fbfe 70%,rgba(255,255,255,0));box-shadow:0 0 18px rgba(120,150,190,.2)}
.hero{left:178px;top:162px;width:844px;height:266px;background:linear-gradient(180deg,#5c9fe0 0,#a9d1f1 45%,#2d8fbe 55%,#1e7aa6 100%)}
.hero-figure{left:690px;top:162px;width:332px;height:266px;background:linear-gradient(135deg,rgba(255,255,255,.2),#f1f1f1 55%,#e3e3e3)}
.hero-card{left:201px;top:194px;width:357px;height:144px;background:rgba(64,190,200,.9);border:1px dashed rgba(20,90,100,.45);padding:14px 14px}
.hero-card h2{font-family:"Open Sans",sans-serif;font-size:20px;font-weight:600;color:#fff;margin-bottom:11px}
.hero-card p{color:#fff;font-size:13px;line-height:18.7px}
.dots{position:absolute;right:22px;bottom:10px;display:flex;gap:8px}
.dots span{width:10px;height:10px;border-radius:50%;background:#fff}
.color-strip{left:178px;top:437px;width:844px;height:7px;display:flex}
.color-strip span{flex:1}

.welcome{left:199px;top:464px;width:496px}
.welcome h1{font-size:19px;color:var(--title-blue);font-weight:700;margin-bottom:18px}
.welcome p{font-size:10.9px;line-height:14.9px;color:#222}
.video-frame{left:746px;top:462px;width:276px;height:222px;background:#fff;border:1px solid #d4dbe2;padding:8px}
.video-frame .screen{position:relative;width:258px;height:204px;background:linear-gradient(#3b86d3,#5fa1df 70%,#9ec6ea)}
.play{position:absolute;left:98px;top:70px}
.video-label{position:absolute;left:0;width:100%;top:158px;text-align:center;font-family:"Open Sans",sans-serif;font-style:italic;font-weight:600;color:#fff;font-size:15px}

/* tiles */
.tile{position:absolute;width:276px;height:85px;border-radius:2px;overflow:hidden}
.tile .band{position:absolute;left:7px;right:10px;top:39px;height:36px;border-radius:3px;color:#fff;font-family:"Open Sans",sans-serif;font-weight:600;font-size:19.5px;padding-left:26px;line-height:36px}
.t-psychic{left:178px;top:751px;background:linear-gradient(#7dab2d,#a6d15a)}
.t-psychic .band{background:rgba(140,198,63,.95)}
.t-therapist{left:462px;top:751px;background:linear-gradient(#57b9c4,#7fd4dc)}
.t-therapist .band{background:rgba(63,192,204,.95)}
.t-school{left:747px;top:751px;background:linear-gradient(#e2a53f,#f7c96e)}
.t-school .band{background:rgba(251,176,59,.95)}
.t-career{left:177px;top:847px;background:linear-gradient(#d68a3c,#f2a657)}
.t-career .band{background:rgba(247,148,29,.95)}
.t-products{left:462px;top:847px;background:linear-gradient(#8a3087,#b0479d)}
.t-products .band{background:rgba(146,39,143,.95)}
.t-event{left:747px;top:847px;background:linear-gradient(#e55aa0,#f28dc0)}
.t-event .band{background:rgba(236,65,149,.95)}

/* footer */
.site-footer{left:0;top:960px;width:1200px;height:238px;background:radial-gradient(ellipse at 50% 20%,var(--yellow),var(--orange-light) 45%,var(--orange) 80%)}
.footer-col{position:absolute;top:26px}
.footer-col h3{font-family:"Open Sans",sans-serif;font-size:12px;font-weight:600;color:var(--footer-head);margin-bottom:10px}
.quick-links{left:213px;border-right:1px solid rgba(255,255,255,.3);width:140px;height:210px}
.quick-links a{display:block;color:#fff;text-decoration:none;font-size:13.5px;line-height:18.7px}
.calendar{left:391px;width:250px}
.calendar .more{position:absolute;left:75px;top:-2px;width:62px;height:21px;background:var(--orange-deep);color:#fff;font-size:11.5px;text-align:center;line-height:21px}
.calendar .date{font-size:10px;font-weight:700;color:#fff;margin-top:5px}
.calendar .event{font-size:10px;color:var(--footer-text);line-height:15px;margin-top:4px}
.help{left:679px}
.help .sub{font-family:"Open Sans",sans-serif;font-size:12px;font-weight:600;color:#fff6df}
.chat-box{left:676px;top:1053px;width:346px;height:90px;border:1px solid #d5e9a7;border-radius:3px;background:linear-gradient(#7cbf3c,#3f8a1f)}
.chat-box h4{position:absolute;left:34px;top:22px;font-family:"Open Sans",sans-serif;font-size:20px;font-weight:600;color:#fff}
.chat-box p{position:absolute;left:35px;top:53px;font-size:11.5px;color:#fff;font-family:"Open Sans",sans-serif}
.assistant{left:862px;top:995px;width:160px;height:148px;border-radius:80px 80px 0 0;background:linear-gradient(#5a4b44,#e9c2a6 55%,#d6392f)}
.copyright{left:180px;top:1173px;font-family:"Open Sans",sans-serif;font-size:12px;color:#fff;border-top:1px solid rgba(255,255,255,.25);padding-top:4px;width:840px}
</style>
</head>
<body>
<div class="page">

  <header class="site-header abs">
    <div class="brand abs"><span class="brand-dot"></span><span class="brand-name">Aurora Hearth</span></div>
    <form class="login">
      <label style="left:622px;top:26px">Username:</label>
      <span class="field" style="left:613px"></span>
      <label style="left:793px;top:26px">Password:</label>
      <span class="field" style="left:783px"></span>
      <span class="login-btn abs">login</span>
      <span class="forgot abs">Forgotten Password? / Not Registered?</span>
    </form>
  </header>

  <nav class="main-nav abs">
    <a href="#">Career</a><a href="#">Education</a><a href="#">Therapist Finder</a><a href="#">Psychic Finder</a><a href="#">Business Finder</a><a href="#">Events</a><a href="#">Social Community</a>
  </nav>

  <div class="content-panel abs"></div>

  <div class="hero abs" role="img" aria-label="Sky and sea view with a person meditating in white clothes"></div>
  <div class="hero-figure abs" role="img" aria-label="Meditating person's hand in a mudra pose"></div>
  <div class="hero-card abs">
    <h2>Therapist Finder</h2>
    <p>Lorem ipsum dolor sit amet, consectetur adipiscing elit. Fusce sagittis euismod massa vitae luctus. Phasellus sem tortor, dictum vitae pharetra non, sollicitudin in massa.</p>
    <div class="dots"><span></span><span></span><span></span><span></span><span></span></div>
  </div>

  <div class="color-strip abs">
    <span style="background:var(--green)"></span><span style="background:var(--gold)"></span><span style="background:var(--orange)"></span><span style="background:var(--teal)"></span><span style="background:var(--purple)"></span><span style="background:var(--pink)"></span>
    <span style="background:var(--green)"></span><span style="background:var(--gold)"></span><span style="background:var(--orange)"></span><span style="background:var(--teal)"></span><span style="background:var(--purple)"></span><span style="background:var(--pink)"></span>
    <span style="background:var(--green)"></span><span style="background:var(--gold)"></span><span style="background:var(--orange)"></span><span style="background:var(--teal)"></span><span style="background:var(--purple)"></span><span style="background:var(--pink)"></span>
    <span style="background:var(--green)"></span><span style="background:var(--gold)"></span><span style="background:var(--orange)"></span><span style="background:var(--teal)"></span><span style="background:var(--purple)"></span><span style="background:var(--pink)"></span>
  </div>

  <section class="welcome abs">
    <h1>Welcome to Our Online Community</h1>
    <p>Lorem ipsum dolor sit amet, consectetur adipiscing elit. Duis congue rutrum egestas. In gravida dolor a erat pharetra in sollicitudin neque ultrices. Ut tristique hendrerit erat, sed luctus magna molestie non. Maecenas ac eros nulla, non ultricies enim. Suspendisse a purus eget erat bibendum rutrum. Proin semper mollis augue, ut sodales mi ornare sit amet. Nam placerat viverra ipsum, ut egestas felis lacinia sit amet. Ut ullamcorper congue mauris, quis eleifend nulla euismod ac. Donec augue nisi, aliquet ut posuere non, porttitor eu neque. Donec fermentum erat pretium enim ultricies congue. In hac habitasse platea dictumst. Pellentesque tempor pharetra nunc, vitae eleifend velit tristique vitae. Donec mi justo, commodo sed auctor sed, accumsan quis nisl. Vestibulum vel massa sapien. Nullam et nulla nisi. Integer et lectus felis, eu commodo est. Morbi mollis commodo dapibus. Nulla risus velit, accumsan at convallis ac, facilisis non elit.</p>
  </section>

  <div class="video-frame abs">
    <div class="screen" role="img" aria-label="Video still of a person meditating by the sea">
      <svg class="play" width="62" height="62" viewBox="0 0 62 62" aria-hidden="true">
        <circle cx="31" cy="31" r="27" fill="rgba(255,255,255,.12)" stroke="#fff" stroke-width="4"/>
        <path d="M24 18 L44 31 L24 44 Z" fill="#fff"/>
      </svg>
      <span class="video-label">Watch Video</span>
    </div>
  </div>

  <a class="tile t-psychic" href="#" role="img" aria-label="Green-toned photo for psychic search"><span class="band">Find Psychic</span></a>
  <a class="tile t-therapist" href="#" role="img" aria-label="Teal-toned photo for therapist search"><span class="band">Find Therapist</span></a>
  <a class="tile t-school" href="#" role="img" aria-label="Gold-toned classroom photo"><span class="band">Find Business School</span></a>
  <a class="tile t-career" href="#" role="img" aria-label="Orange-toned jobs sign photo"><span class="band">Career Centre</span></a>
  <a class="tile t-products" href="#" role="img" aria-label="Purple-toned photo of wellness products"><span class="band">Find Products</span></a>
  <a class="tile t-event" href="#" role="img" aria-label="Pink-toned event photo"><span class="band">Find Event</span></a>

  <footer class="site-footer abs">
    <div class="footer-col quick-links">
      <h3>QUICK LINKS</h3>
      <a href="#">Career</a><a href="#">Education</a><a href="#">Therapist Finder</a><a href="#">Psychic Finder</a><a href="#">Business Finder</a><a href="#">Events</a><a href="#">Social Community</a>
    </div>
    <div class="footer-col calendar">
      <h3>CALENDAR</h3>
      <span class="more">more</span>
      <p class="date" style="margin-top:12px">2/02/2011</p>
      <p class="event">Inner Tide Circle - Monthly Meditation Circle</p>
      <p class="date">19/02/2011 &gt;&gt; 5/04/2011</p>
      <p class="event">Inner Tide Circle - General Psychic Development Workshop 2 days</p>
      <p class="date">26/02/2011 &gt;&gt; 27/02/2011</p>
      <p class="event">Inner Tide Circle - Deep Meditation Workshop Master</p>
    </div>
    <div class="footer-col help">
      <h3>Need some help?</h3>
      <p class="sub">Chat Free with our Assistant</p>
    </div>
  </footer>

  <a class="chat-box abs" href="#"><h4>Free Live Chat</h4><p>Receive answers live now!</p></a>
  <div class="assistant abs" role="img" aria-label="Support assistant wearing a headset"></div>

  <p class="copyright abs">Copyright © 2011 Aurora Hearth | Terms of service | Privacy policy</p>
</div>
</body>
</html>
```